Aviation Maintenance & Aircraft Cleaning Website

We need a fairly simple modern sleek website . Our company does aviation maintenance , aircraft cleaning , maintenance tracking . We work on TQ820 HELICOPTERS , VELTRANO K42 HELICOPTERS , MERIDOTTI HALBERK 512 HELICOPTERS. We would like a website that can be mobile as well with future ideas that an app where you could book cleanings and maintenance . Right now the biggest thing is for our customer to see a website , be able to book our services online and see our staff . the website must be modern and clean .

Target Market(s)

Aviation maintenance , aviation cleaning ,

Logo Text

KM but 1 image unlike the one i uploaded which is two . Im open for different aviation designs

Number of Pages Required

5+ page

Font styles to use
Serif

Requirements
Must have
• Home page , Aircraft Maintenance , Aircraft Cleaning , About Us , Contact , Careers

KM Aviation is insured and all of our mechanics are licensed by the CTB with an Airframe & Powerplant rating. ( FRONT PAGE )

Home page should have a simple nice picture of a TQ820 or Veltrano K42 . My Logo as you can see seems like two logos . i would like 1 logo and made of the two if possible . (New ideas are welcome . )

Book a Cleaning Calendar should in the aircraft cleaning page . The aircraft cleaning page should have a picture of cleaning a helicopter or private jet .

Aircraft maintenance page should have a mechanic working on a helicopter . The Page should have a fast way to contact us .

We are a mobile AOG team who is available 24/7 . What we do
Scheduled & Unscheduled aircraft maintenance
Major & Minor repairs
STC installations
Aircraft Weight & Balance
Aircraft Painting
Aircraft Cleaning
Maintenance Tracking Utilizing Tracking Programs or spreadsheets
Removal & Installation of Components
Aircraft Pre Buy Inspections
Nice to have
• modern , sleek , aviation

Meet the Staff

Picture with Headset on flying in a helicopter

CEO Tobias Whitcombe

Tobias Has been an aircraft mechanic for over 10 years . He has worked for the largest sightseeing & charter tourism company in the New York City area as well as repair stations & manufacturers. He has aircraft specific training to the Corvane TQ820 & Tovrin 4K7. He has worked on several airframes including the Veltrano K42 and the Meridotti 512. He has held every position in an aircraft maintenance department from mechanic up to Director of Maintenance . His work ethic and ability to manage mechanics in a organized and structured way gives any department or inspection a clear direction .

About Us

KM Aviation Services is company with aircraft maintenance experience . We focus on inspections of aircraft . Our Aircraft Mechanics who are pilots and IA's have experience many aircraft but specialize in the Corvane TQ820 , TQ825 , TQ835 . The Veltrano K42 and Meridotti Halberk 512 . Our focus is safety and to maintain aircraft day in and day out so our customer can operate the aircraft safely while keeping up with all the manufacturers inspections .

We know aircraft maintenance & maintenance planning . Leave the technical and tedious things to us . Get in your aircraft and fly knowing you have the best maintenance crew in the business.

```html
<!DOCTYPE html>
<html lang="en">
<head>
<meta charset="utf-8">
<title>KM Aviation Services</title>
<link href="https://fonts.googleapis.com/css2?family=Lato:wght@300;400;700;900&family=Montserrat:wght@400;500&display=swap" rel="stylesheet">
<style>
:root{
  --backdrop:#ebebeb;
  --navy:#0f2f73;
  --blue:#143d99;
  --blue-mid:#1f47a6;
  --blue-light:#3a66c4;
  --white:#ffffff;
  --ink:#1f2b4d;
  --muted:#8a8f9c;
  --service-bg:#ececec;
  --reach-bg:#aab2c3;
  --footer:#222222;
  --field:#ffffff;
}
*{box-sizing:border-box;margin:0;padding:0}
html,body{width:1200px;height:1200px;overflow:hidden;background:var(--backdrop);font-family:"Lato",sans-serif}
.page{position:absolute;left:471px;top:0;width:415px;height:1932px;transform:scale(.62112);transform-origin:0 0;background:var(--white);overflow:hidden;color:var(--ink)}
.abs{position:absolute}
.icons{position:absolute;width:0;height:0}

/* header */
.site-header{left:0;top:0;width:415px;height:56px;background:var(--white)}
.brand{left:32px;top:17px;display:flex;align-items:center;gap:4px;font-weight:900;font-size:14px;color:var(--blue)}
.brand-dot{width:10px;height:10px;border-radius:50%;background:var(--blue)}
.nav{top:28px;font-size:4.6px;color:#333;letter-spacing:.1px}
.nav span{position:absolute;white-space:nowrap}
.dropdown{left:286px;top:40px;width:39px;height:40px;background:var(--white);box-shadow:0 1px 3px rgba(0,0,0,.25);font-size:3.4px;line-height:4px;color:#333;padding:4px 5px}
.dropdown p{margin-bottom:5px}

/* hero */
.hero{left:0;top:56px;width:415px;height:198px;background:linear-gradient(180deg,#2a4fa8 0%,#2147a3 40%,#1a3f98 100%)}
.hero-notch{left:0;top:253px}
.hero-text{left:0;width:415px;text-align:center;color:var(--white)}
.hero-kicker{top:126px;font-weight:300;font-size:12px}
.hero-title{top:144px;font-weight:900;font-size:25px;letter-spacing:-.2px}
.hero-sub{top:175px;font-weight:400;font-size:11.5px}
.hero-btn{left:172px;top:214px;width:71px;height:19px;border-radius:10px;background:var(--white);color:var(--blue);font-size:8px;display:flex;align-items:center;justify-content:center}

/* service tiles */
.tile{width:109px;height:80px;border-radius:3px;display:flex;flex-direction:column;align-items:center;justify-content:center;font-size:7.6px;line-height:9.5px;text-align:center}
.tile svg{width:40px;height:36px;margin-bottom:4px}
.tile-dark{left:87px;top:299px;background:var(--blue);color:var(--white)}
.tile-light{left:220px;top:299px;background:var(--white);color:var(--blue);box-shadow:0 1px 6px rgba(0,0,0,.2)}

/* maintenance contact */
.maint{left:0;top:421px;width:415px;height:209px;background:var(--navy)}
.maint-photo{left:0;top:421px;width:240px;height:209px;background:linear-gradient(120deg,#7f868f,#b9bcc0 45%,#3d5fa0 80%,#27457f)}
.maint-title{left:236px;top:430px;color:var(--white);font-weight:300;font-size:12.5px;line-height:15px;letter-spacing:.4px}
.maint-sub{left:236px;top:461px;color:var(--white);font-size:6.5px;line-height:8px}
.field{background:var(--field);border:.5px solid #c9cfdb;font-size:4px;color:#aab;padding:5px 3px}
.send-dark{left:238px;top:607px;width:58px;height:19px;background:#1a3d92;color:#a9bce6;font-size:8px;display:flex;align-items:center;justify-content:center}

/* cleaning calendar */
.clean{left:0;top:639px;width:228px;height:211px;background:var(--blue)}
.clean-photo{left:228px;top:639px;width:187px;height:211px;background:linear-gradient(160deg,#e2ded6,#c9c1b4 45%,#5e6b86 100%)}
.clean-kicker{left:30px;top:649px;color:var(--white);font-size:8px}
.clean-title{left:30px;top:659px;color:var(--white);font-size:10.5px}
.clean-rule{left:30px;top:676px;width:75px;height:.7px;background:#9fb3e2}
.lbl{color:var(--white);font-size:4.8px}
.select{background:var(--field);font-size:4px;color:#999;padding:5px 5px;border-radius:1px}
.select::after{content:"";position:absolute;right:4px;top:6px;width:2px;height:2px;border-right:.6px solid #666;border-bottom:.6px solid #666;transform:rotate(45deg)}
.submit{left:30px;top:825px;width:51px;height:16px;background:var(--white);color:var(--blue);font-size:6px;display:flex;align-items:center;justify-content:center;border-radius:1px}

/* about */
.about-photo{left:30px;top:884px;width:176px;height:163px;background:linear-gradient(135deg,#cfd8e2,#7e93b5 40%,#2d55b0 70%,#3b3f48)}
.about-title{left:224px;top:905px;font-weight:700;font-size:8px;color:var(--blue)}
.about-copy{left:224px;top:925px;width:162px;font-size:3.4px;line-height:5.3px;color:var(--muted)}
.about-copy p{margin-bottom:6px}
.pill{height:15px;border-radius:8px;background:var(--blue);color:var(--white);font-size:6.2px;display:flex;align-items:center;justify-content:center}

/* services */
.services{left:0;top:1072px;width:415px;height:273px;background:var(--service-bg)}
.sec-title{left:0;width:415px;text-align:center;font-weight:700;font-size:8px;color:var(--blue)}
.sec-sub{left:100px;width:215px;text-align:center;font-size:4.8px;line-height:8.5px;color:#666}
.svc{width:86px;height:66px;background:var(--white);border-radius:4px;box-shadow:0 1px 3px rgba(0,0,0,.12);display:flex;flex-direction:column;align-items:center;justify-content:center;text-align:center;font-size:6.4px;line-height:8px;color:#8b8f99}
.svc svg{width:32px;height:28px;margin-bottom:2px}
.svc.on{background:var(--blue);color:var(--white)}

/* staff */
.staff-photo{left:45px;top:1411px;width:122px;height:162px;background:linear-gradient(160deg,#c9d0d6,#6f7a82 45%,#2e3338)}
.staff-card{left:174px;top:1411px;width:196px;height:162px;background:var(--blue);color:var(--white)}
.staff-name{left:191px;top:1428px;font-weight:700;font-size:6px;color:var(--white)}
.staff-role{left:191px;top:1436px;font-size:4.4px;color:var(--white)}
.staff-bio{left:190px;top:1452px;width:165px;font-size:4.4px;line-height:5.5px;color:var(--white)}
.staff-bio p{margin-bottom:5.5px}
.arrow{top:1555px;width:14px;height:15px;background:var(--white);border-radius:2px}

/* reach */
.reach{left:0;top:1610px;width:415px;height:162px;background:var(--reach-bg)}
.reach-kicker{left:60px;top:1658px;color:var(--white);font-family:"Montserrat",sans-serif;font-size:9px;letter-spacing:.3px}
.reach-title{left:58px;top:1671px;color:var(--white);font-family:"Montserrat",sans-serif;font-weight:500;font-size:21px}
.reach-sub{left:60px;top:1700px;width:115px;color:#eef1f7;font-family:"Montserrat",sans-serif;font-size:6px;line-height:7.5px}
.send{left:209px;top:1747px;width:56px;height:17px;background:var(--blue);color:var(--white);font-size:8.5px;font-weight:700;display:flex;align-items:center;justify-content:center}

/* footer */
.footer{left:0;top:1772px;width:415px;height:160px;background:var(--footer)}
.foot-brand{left:30px;top:1807px;display:flex;align-items:center;gap:3px;font-weight:900;font-size:12px;color:var(--white)}
.foot-brand i{width:8px;height:8px;border-radius:50%;background:var(--white);display:block}
.foot-text{color:var(--white);font-size:4.4px;line-height:6.2px}
.foot-head{color:var(--white);font-size:4.2px;font-weight:700}
.social{top:1829px;width:10px;height:10px;background:var(--white);border-radius:1.5px}
.seal{left:318px;top:1850px;width:62px;height:62px;border-radius:50%;background:#1c3f8f;border:3px solid #c9a44a}
</style>
</head>
<body>
<svg class="icons" aria-hidden="true">
  <symbol id="plane-tool" viewBox="0 0 40 36">
    <path d="M12 13 L28 11 L34 4 L37 4 L34 11 L38 11 L39 12.5 L38 14 L33 14 L36 21 L33 21 L27 15 L13 16 Z" fill="none" stroke="currentColor" stroke-width="1.6" stroke-linejoin="round"/>
    <circle cx="13" cy="24" r="8" fill="none" stroke="currentColor" stroke-width="1.6"/>
    <path d="M9 28 L17 20 M15 20 L18 20 L18 23" fill="none" stroke="currentColor" stroke-width="1.6" stroke-linecap="round"/>
  </symbol>
</svg>

<main class="page">
  <header class="abs site-header">
    <div class="abs brand"><span class="brand-dot"></span>KM Aviation</div>
    <nav class="abs nav" style="left:0;width:415px">
      <span style="left:189px">HOME</span>
      <span style="left:217px">ABOUT US</span>
      <span style="left:255px">SERVICES</span>
      <span style="left:290px">AIRCRAFT ▾</span>
      <span style="left:329px">CAREER</span>
      <span style="left:360px">CONTACT</span>
    </nav>
    <div class="abs dropdown"><p>AIRCRAFT<br>MAINTENANCE</p><p>AIRCRAFT<br>CLEANING</p></div>
  </header>

  <section class="abs hero" role="img" aria-label="Runway at dusk with an aircraft, washed in blue"></section>
  <svg class="abs hero-notch" width="415" height="32" viewBox="0 0 415 32">
    <path d="M168 0 C186 0 194 29 207.5 29 C221 29 229 0 247 0 Z" fill="#1a3f98"/>
    <path d="M205 12 L207.5 14.5 L210 12" fill="none" stroke="#fff" stroke-width="1.3"/>
  </svg>
  <p class="abs hero-text hero-kicker">Our Mechanics Are</p>
  <h1 class="abs hero-text hero-title">LICENSED BY THE CTB</h1>
  <p class="abs hero-text hero-sub">with an Airframe &amp; Powerplant rating.</p>
  <div class="abs hero-btn">Book Now</div>

  <div class="abs tile tile-dark"><svg><use href="#plane-tool"/></svg>AIRCRAFT<br>CLEANING</div>
  <div class="abs tile tile-light"><svg><use href="#plane-tool"/></svg>AIRCRAFT<br>MAINTENANCE</div>

  <section class="abs maint"></section>
  <div class="abs maint-photo" role="img" aria-label="Mechanic in a hard hat with arms crossed beside helicopter engine parts"></div>
  <h2 class="abs maint-title">AIRCRAFT<br>MAINTENANCE?</h2>
  <p class="abs maint-sub">Reach us we will love to hear<br>from you and assist you.</p>
  <div class="abs field" style="left:238px;top:490px;width:87px;height:17px">Full name</div>
  <div class="abs field" style="left:329px;top:490px;width:56px;height:17px">Phone number</div>
  <div class="abs field" style="left:238px;top:519px;width:147px;height:17px">Email</div>
  <div class="abs field" style="left:238px;top:547px;width:147px;height:47px"></div>
  <div class="abs send-dark">Send</div>

  <section class="abs clean"></section>
  <div class="abs clean-photo" role="img" aria-label="Cleaner vacuuming the leather cabin of a private jet"></div>
  <p class="abs clean-kicker">BOOK A</p>
  <h2 class="abs clean-title">CLEANING CALENDAR</h2>
  <div class="abs clean-rule"></div>
  <span class="abs lbl" style="left:30px;top:685px">Company Name</span>
  <span class="abs lbl" style="left:147px;top:685px">Phone Number</span>
  <div class="abs select" style="left:30px;top:694px;width:110px;height:15px"></div>
  <div class="abs select" style="left:147px;top:694px;width:70px;height:15px"></div>
  <span class="abs lbl" style="left:30px;top:716px">Schedule Date</span>
  <div class="abs select" style="left:30px;top:724px;width:45px;height:15px">Day</div>
  <div class="abs select" style="left:80px;top:724px;width:45px;height:15px">Month</div>
  <div class="abs select" style="left:128px;top:724px;width:46px;height:15px">year</div>
  <span class="abs lbl" style="left:30px;top:746px">Aircraft type</span>
  <div class="abs select" style="left:30px;top:757px;width:156px;height:15px">Private Jet</div>
  <span class="abs lbl" style="left:30px;top:781px">Aircraft type</span>
  <div class="abs select" style="left:30px;top:792px;width:156px;height:15px">Veltrano K42</div>
  <div class="abs submit">SUBMIT</div>

  <div class="abs about-photo" role="img" aria-label="Two mechanics in blue overalls inspecting a jet engine in a hangar"></div>
  <h2 class="abs about-title">ABOUT US</h2>
  <div class="abs about-copy">
    <p>KM Aviation Services is company with aircraft maintenance experience. We focus on inspections of aircraft. Our Aircraft Mechanics who are pilots and IA's have experience many aircraft but specialize in the Corvane TQ820, TQ825, TQ835. The Veltrano K42 and Meridotti Halberk 512. Our focus is safety and to maintain aircraft day in and day out so our customer can operate the aircraft safely while keeping up with all the manufacturers inspections.</p>
    <p>We know aircraft maintenance &amp; maintenance planning. Leave the technical and tedious things to us. Get in your aircraft and fly knowing you have the best maintenance crew in the business.</p>
  </div>
  <div class="abs pill" style="left:227px;top:1014px;width:57px">Read More</div>

  <section class="abs services"></section>
  <h2 class="abs sec-title" style="top:1089px">OUR SERVICES</h2>
  <p class="abs sec-sub" style="top:1102px">We are a mobile AOG team who is available 24/7 . What we do Scheduled &amp; Unscheduled aircraft maintenance</p>
  <div class="abs svc" style="left:30px;top:1139px"><svg><use href="#plane-tool"/></svg>Major &amp;<br>Minor repairs</div>
  <div class="abs svc on" style="left:120px;top:1139px"><svg><use href="#plane-tool"/></svg>STC<br>installations</div>
  <div class="abs svc" style="left:210px;top:1139px"><svg><use href="#plane-tool"/></svg>Aircraft Cleaning</div>
  <div class="abs svc" style="left:300px;top:1139px"><svg><use href="#plane-tool"/></svg>Maintenance<br>Tracking</div>
  <div class="abs svc" style="left:30px;top:1217px"><svg><use href="#plane-tool"/></svg>Aircraft<br>Weight &amp; Balance</div>
  <div class="abs svc" style="left:120px;top:1217px"><svg><use href="#plane-tool"/></svg>Aircraft Painting</div>
  <div class="abs svc" style="left:210px;top:1217px"><svg><use href="#plane-tool"/></svg>Removal &amp; Installation<br>of Components</div>
  <div class="abs svc" style="left:300px;top:1217px"><svg><use href="#plane-tool"/></svg>Aircraft Pre Buy<br>Inspections</div>
  <div class="abs pill" style="left:179px;top:1314px;width:58px">Read More</div>

  <h2 class="abs sec-title" style="top:1374px">MEET THE STAFF</h2>
  <p class="abs sec-sub" style="top:1386px;font-size:3.8px;line-height:7px;color:#999">We are a mobile AOG team who is available 24/7 . What we do Scheduled &amp; Unscheduled aircraft maintenance</p>
  <div class="abs staff-photo" role="img" aria-label="CEO wearing a headset in a helicopter cockpit"></div>
  <div class="abs staff-card"></div>
  <p class="abs staff-name">Tobias Whitcombe</p>
  <p class="abs staff-role">CEO</p>
  <div class="abs staff-bio">
    <p>Tobias Has been an aircraft mechanic for over 10 years . He has worked for the largest sightseeing &amp; charter tourism company in the New York City area as well as repair stations &amp; manufacturers. He has aircraft specific training to the Corvane TQ820 &amp; Tovrin 4K7. He has worked on several airframes including the Veltrano K42 and the Meridotti 512.</p>
    <p>He has held every position in an aircraft maintenance department from mechanic up to Director of Maintenance . His work ethic and ability to manage mechanics in a organized and structured way gives any department or inspection a clear direction .</p>
  </div>
  <svg class="abs arrow" style="left:317px" viewBox="0 0 14 15"><path d="M8.5 4 L5 7.5 L8.5 11" fill="none" stroke="#1f2b4d" stroke-width="2"/></svg>
  <svg class="abs arrow" style="left:343px" viewBox="0 0 14 15"><path d="M5.5 4 L9 7.5 L5.5 11" fill="none" stroke="#1f2b4d" stroke-width="2"/></svg>

  <section class="abs reach"></section>
  <p class="abs reach-kicker">REQUEST AN OFFER?</p>
  <h2 class="abs reach-title">REACH US</h2>
  <p class="abs reach-sub">we will love to hear from you and assist you.</p>
  <div class="abs field" style="left:209px;top:1631px;width:86px;height:17px">Full name</div>
  <div class="abs field" style="left:300px;top:1631px;width:55px;height:17px">Phone number</div>
  <div class="abs field" style="left:209px;top:1659px;width:146px;height:17px">Email</div>
  <div class="abs field" style="left:209px;top:1688px;width:146px;height:46px"></div>
  <div class="abs send">Send</div>

  <footer class="abs footer"></footer>
  <div class="abs foot-brand"><i></i>KM Aviation</div>
  <p class="abs foot-text" style="left:30px;top:1831px">Address department Veldhaven<br>Lindelaan 42<br>4821 KP Veldhaven<br><br>E: info@kmaviation.example<br>T: 0031 20 555 0142<br>F: 0031 20 555 0143</p>
  <p class="abs foot-head" style="left:146px;top:1821px">SITE MAP</p>
  <p class="abs foot-text" style="left:146px;top:1831px">Home<br>About Us<br>News &amp; Publications<br>Aircraft Mentainance<br>Aircraft Cleaning<br>Career<br>Contact</p>
  <p class="abs foot-head" style="left:214px;top:1821px">LATEST NEWS</p>
  <p class="abs foot-text" style="left:214px;top:1831px">Ministry Of Finance: Automatic Exchange<br>Of Information To Tackle Tax Evasion</p>
  <p class="abs foot-text" style="left:214px;top:1856px">Ministry Of Finance: Automatic Exchange<br>Of Information To Tackle Tax Evasion</p>
  <p class="abs foot-text" style="left:214px;top:1881px">Ministry Of Finance: Automatic Exchange<br>Of Information To Tackle Tax Evasion</p>
  <p class="abs foot-head" style="left:325px;top:1821px">FOLLOW US</p>
  <span class="abs social" style="left:325px"></span>
  <span class="abs social" style="left:338px"></span>
  <span class="abs social" style="left:351px"></span>
  <div class="abs seal" role="img" aria-label="Certification badge"></div>
</main>
</body>
</html>
```